Landing Page for Bathroom Remodeling Webpage - Desktop and Mobile

I am looking for some help designing the "above the fold" area for my bathroom remodeling service page. Looking for something a little different than the rest. Typically remodeling companies just put a nice picture of a bathroom remodel but I would like to do something a little different / more creative. Below is a link to the current wireframe we are working on.
Current website is located at plumvantaridge.com
Again the biggest thing I am looking for is a design for the very top section but would love help on the rest of the page as well. You will see by viewing the link below the type of information we are looking to include on the page:
PLEASE DO INCLUDE WHAT THE MOBILE VERSION WOULD LOOK LIKE AS WELL.
Wireframe:
https://boards.quillmerra.com/view/3f8a1b2c-90de-4e7a-b5c1-aa62d09e1f35-418k/
There are also comments in the link above you can read as well.
We like the idea of something interactive such as this...
https://pixorvale.com/shots/5192746-Glenhart-Scooter-Store-Animation
Attached is also the logo we want to use going forward
Target Market(s)
Residential homeowners, 30 years old+ with professional careers
Number of Pages Required
1 page
Look and feel
Each slider illustrates characteristics of the customer's brand and the style your logo design should communicate.

```html
<!DOCTYPE html>
<html lang="en">
<head>
<meta charset="utf-8">
<title>Hearthline – Home Remodeling</title>
<link rel="stylesheet" href="https://fonts.googleapis.com/css2?family=Montserrat:wght@400;500;600;700;800&family=Poppins:wght@300;400;500;600&family=Dancing+Script:wght@400&display=swap">
<style>
:root{
  --red:#d41c1c;
  --red-dark:#b51212;
  --navy:#223b66;
  --navy-deep:#1b2f55;
  --blue:#3e8bf0;
  --paper:#f6f6f6;
  --ink:#1f2f52;
  --muted:#8a8f99;
  --white:#ffffff;
}
*{box-sizing:border-box;margin:0;padding:0}
html,body{width:1200px;height:3764px;overflow:hidden}
body{position:relative;font-family:"Poppins",sans-serif;color:var(--ink);background:var(--paper)}
.abs{position:absolute}
.center{text-align:center;left:0;width:1200px}

/* header */
.site-header{position:absolute;top:0;left:0;width:1200px;height:60px;background:#fff;z-index:5;box-shadow:0 1px 4px rgba(0,0,0,.08)}
.brand{position:absolute;left:92px;top:15px;display:flex;align-items:center;gap:10px;font-family:"Montserrat",sans-serif;font-weight:800;font-size:25px;color:var(--red);letter-spacing:.5px}
.brand-dot{width:28px;height:28px;border-radius:50%;background:var(--navy)}
.nav{position:absolute;top:24px;font-family:"Montserrat",sans-serif;font-size:11px;font-weight:500;color:#333;letter-spacing:.3px;white-space:nowrap}
.nav .caret{font-size:7px;color:#999;margin-left:2px}
.estimate{position:absolute;left:984px;top:0;width:122px;height:73px;background:var(--navy-deep);color:#fff;text-align:center;padding-top:15px;z-index:6}
.estimate small{display:block;font-size:10px;opacity:.85}
.estimate strong{display:block;font-family:"Montserrat",sans-serif;font-size:14px;font-weight:700;margin-top:2px}

/* hero */
.hero{position:absolute;top:60px;left:0;width:1200px;height:533px;overflow:hidden}
.hero svg{position:absolute;inset:0}
.hero-title{position:absolute;top:186px;left:0;width:1200px;text-align:center;font-family:"Montserrat",sans-serif;font-weight:800;font-size:52px;line-height:52px;color:#fff}
.hero-sub{position:absolute;top:306px;left:0;width:1200px;text-align:center;font-size:16px;line-height:25px;color:#fff;font-weight:300}
.btn-hero{position:absolute;left:501px;top:389px;width:198px;height:58px;border-radius:29px;background:linear-gradient(118deg,var(--blue) 0 55%,var(--red) 55%);color:#fff;font-family:"Montserrat",sans-serif;font-size:13px;font-weight:600;display:flex;align-items:center;justify-content:center}

/* section titles */
.eyebrow{font-family:"Dancing Script",cursive;color:var(--red);font-size:22px}
.section-title{font-family:"Montserrat",sans-serif;font-weight:700;font-size:21px;letter-spacing:2px;color:var(--ink)}
.wave{position:absolute}

/* services */
.services{position:absolute;top:593px;left:0;width:1200px;height:876px;background:var(--paper)}
.service-card{position:absolute;width:231px;height:196px;background:#fff;box-shadow:0 2px 10px rgba(0,0,0,.09);text-align:center}
.service-icon{position:absolute;left:71px;top:-44px;width:88px;height:88px;border-radius:50%;border:2px solid var(--red);background:#fff;display:flex;align-items:center;justify-content:center}
.service-card h3{margin-top:82px;font-family:"Montserrat",sans-serif;font-weight:400;font-size:12.5px;letter-spacing:.2px;color:var(--ink);white-space:nowrap}
.service-card p{margin:12px auto 0;width:170px;font-size:11px;line-height:24px;color:var(--muted);font-weight:300}

/* projects */
.projects{position:absolute;top:1469px;left:0;width:1200px;height:608px;background:radial-gradient(ellipse at 50% 45%,#eceef1 0,#f7f7f8 55%,#fdfdfd 100%)}
.project-card{position:absolute;top:187px;width:256px;height:326px;overflow:hidden}
.project-card svg.photo{position:absolute;inset:0}
.project-card h4{position:absolute;left:17px;top:268px;font-family:"Montserrat",sans-serif;font-weight:700;font-size:15px;color:#fff;white-space:nowrap}
.project-loc{position:absolute;left:17px;top:292px;font-size:10px;color:#fff;display:flex;align-items:center;gap:6px;white-space:nowrap}
.project-loc svg{flex-shrink:0}
.load-more{position:absolute;top:556px;left:0;width:1200px;text-align:center;font-family:"Montserrat",sans-serif;font-weight:600;font-size:11px;color:var(--red)}

/* faq */
.faq{position:absolute;top:2077px;left:0;width:1200px;height:592px;overflow:hidden}
.faq svg.bg{position:absolute;inset:0}
.faq-title{position:absolute;top:72px;left:0;width:1200px;text-align:center;font-family:"Montserrat",sans-serif;font-weight:700;font-size:21px;letter-spacing:2px;color:#fff}
.faq-rule{position:absolute;top:106px;left:398px;width:404px;border-top:1px dashed rgba(255,255,255,.55)}
.faq-item{position:absolute;left:300px;width:599px;background:#fff;font-size:15px;color:#555}
.faq-q{height:60px;display:flex;align-items:center;justify-content:space-between;padding:0 26px}
.faq-item.open .faq-q{background:#d5d9e0;height:46px}
.faq-a{padding:11px 26px;font-size:10px;line-height:17px;color:#444}

/* articles */
.articles{position:absolute;top:2669px;left:0;width:1200px;height:685px;background:var(--paper)}
.article-card{position:absolute;top:207px;width:283px;height:379px;background:#fff;border:2px solid #e6e6e6;padding:8px}
.article-media{width:100%;height:178px}
.article-card h5{margin:25px 8px 0;font-family:"Montserrat",sans-serif;font-weight:700;font-size:12px;color:var(--ink);white-space:nowrap}
.article-meta{margin:10px 8px 0;font-size:10px;color:var(--muted);display:flex;align-items:center;gap:8px}
.article-card p{margin:16px 8px 0;width:240px;font-size:12px;line-height:17px;color:#333}
.article-link{margin:18px 8px 0;font-family:"Montserrat",sans-serif;font-size:10px;font-weight:600;color:var(--red)}

/* footer */
.footer{position:absolute;top:3354px;left:0;width:1200px;height:410px;overflow:hidden;color:#fff}
.footer svg.bg{position:absolute;inset:0}
.footer-brand{position:absolute;left:153px;top:60px;display:flex;align-items:center;gap:10px;font-family:"Montserrat",sans-serif;font-weight:800;font-size:25px;color:#fff}
.footer-brand .brand-dot{background:var(--red)}
.footer-about{position:absolute;left:146px;top:130px;width:230px;font-size:10.5px;line-height:20px}
.footer-head{position:absolute;top:70px;font-family:"Montserrat",sans-serif;font-weight:700;font-size:12px;letter-spacing:1.2px;white-space:nowrap}
.footer-head::after{content:"";position:absolute;left:0;top:24px;width:72px;border-top:1px solid rgba(255,255,255,.7)}
.field{position:absolute;left:449px;width:171px;height:32px;background:#2a0606;border:1px solid #4a1a1a;font-size:10px;padding:9px 16px;color:#ddd}
.btn-submit{position:absolute;left:449px;top:228px;width:171px;height:34px;border-radius:17px;background:linear-gradient(90deg,var(--blue),var(--red));font-family:"Montserrat",sans-serif;font-weight:600;font-size:11px;display:flex;align-items:center;justify-content:center}
.footer-list{position:absolute;top:126px;list-style:none;font-size:10.5px;line-height:25.7px;white-space:nowrap}
.copyright{position:absolute;top:366px;left:0;width:1200px;height:44px;background:var(--navy-deep);border-top:1px solid rgba(255,255,255,.12);text-align:center;font-family:"Montserrat",sans-serif;font-weight:600;font-size:9.5px;line-height:44px}
</style>
</head>
<body>

<header class="site-header">
  <div class="brand"><span class="brand-dot"></span>HEARTHLINE</div>
  <nav>
    <span class="nav" style="left:421px">HOME</span>
    <span class="nav" style="left:487px">SERVICES<span class="caret">▾</span></span>
    <span class="nav" style="left:573px">VIDEOS<span class="caret">▾</span></span>
    <span class="nav" style="left:647px">GALLERY<span class="caret">▾</span></span>
    <span class="nav" style="left:728px">BLOG<span class="caret">▾</span></span>
    <span class="nav" style="left:791px">ABOUT<span class="caret">▾</span></span>
    <span class="nav" style="left:862px">CONTACT<span class="caret">▾</span></span>
  </nav>
  <div class="estimate"><small>Get Free Estimate</small><strong>555-014-2290</strong></div>
</header>

<section class="hero">
  <svg width="1200" height="533" role="img" aria-label="Bathroom interior photo under a split navy and red overlay">
    <rect width="1200" height="533" fill="#d82626"/>
    <polygon points="0,0 256,0 1200,525 1200,533 0,533" fill="#2c4a85"/>
    <rect x="0" y="530" width="1200" height="3" fill="#1d335f"/>
  </svg>
  <h1 class="hero-title">MAKING HOMES<br>THAT MATTER.</h1>
  <p class="hero-sub">We provide home remodeling services to help you build a<br>home you love</p>
  <div class="btn-hero">OUR SERVICES</div>
</section>

<section class="services">
  <div class="abs center eyebrow" style="top:60px">Remodeling simplified</div>
  <h2 class="abs center section-title" style="top:97px">HOME REMODELING SERVICES</h2>
  <svg class="wave" style="left:422px;top:130px" width="356" height="6"><path d="M0 3 Q4 0 8 3 T16 3 T24 3 T32 3 T40 3 T48 3 T56 3 T64 3 T72 3 T80 3 T88 3 T96 3 T104 3 T112 3 T120 3 T128 3 T136 3 T144 3 T152 3 T160 3 T168 3 T176 3 T184 3 T192 3 T200 3 T208 3 T216 3 T224 3 T232 3 T240 3 T248 3 T256 3 T264 3 T272 3 T280 3 T288 3 T296 3 T304 3 T312 3 T320 3 T328 3 T336 3 T344 3 T352 3" fill="none" stroke="#3e6ad0" stroke-width="1"/></svg>

  <div class="service-card" style="left:210px;top:258px">
    <div class="service-icon"><svg width="44" height="44" fill="none" stroke="#3e8bf0" stroke-width="2"><rect x="4" y="6" width="36" height="34"/><path d="M4 18h10v8h8v8h8v6"/></svg></div>
    <h3>BASEMENT FINISHING</h3><p>Add additional living space to your home.</p>
  </div>
  <div class="service-card" style="left:476px;top:258px">
    <div class="service-icon"><svg width="44" height="44" fill="none" stroke="#3e8bf0" stroke-width="2"><path d="M4 22 22 6l18 16M9 18v20h26V18"/><rect x="18" y="26" width="8" height="12"/></svg></div>
    <h3>WHOLE HOME REMODELLING</h3><p>Give your entire space the feeling of a brand new home.</p>
  </div>
  <div class="service-card" style="left:759px;top:258px">
    <div class="service-icon"><svg width="44" height="44" fill="none" stroke="#3e8bf0" stroke-width="2"><circle cx="23" cy="22" r="11"/><circle cx="23" cy="22" r="6"/><path d="M6 10v24M40 10v24"/></svg></div>
    <h3>KITCHEN REMODELLING</h3><p>The heart of the home. Make it feel the part.</p>
  </div>
  <div class="service-card" style="left:210px;top:566px">
    <div class="service-icon"><svg width="44" height="44" fill="none" stroke="#3e8bf0" stroke-width="2"><path d="M8 40V16a14 14 0 0 1 28 0v24z"/><path d="M22 4v36M8 22h28M8 31h28M4 40h36"/></svg></div>
    <h3>WINDOW REPLACEMENT</h3><p>Our experienced team has replaced thousands of windows.</p>
  </div>
  <div class="service-card" style="left:476px;top:566px">
    <div class="service-icon"><svg width="44" height="44" fill="none" stroke="#3e8bf0" stroke-width="2"><path d="M22 4v6M10 22a12 12 0 0 1 24 0zM6 22h32"/><path d="M14 28v2M22 28v2M30 28v2M10 34v2M18 34v2M26 34v2M34 34v2" stroke-linecap="round"/></svg></div>
    <h3>BATHROOM REMODELLING</h3><p>Create the spa like bathroom you've dreamed of.</p>
  </div>
  <div class="service-card" style="left:759px;top:566px">
    <div class="service-icon"><svg width="44" height="44" fill="none" stroke="#3e8bf0" stroke-width="2"><circle cx="22" cy="22" r="7"/><path d="M22 4v6M22 34v6M4 22h6M34 22h6M9 9l4 4M31 31l4 4M35 9l-4 4M13 31l-4 4"/><circle cx="22" cy="22" r="13"/></svg></div>
    <h3>HANDYMAN</h3><p>Let us take care of your to do list.</p>
  </div>
</section>

<section class="projects" role="img" aria-label="Soft faded bathroom photo in the background">
  <h2 class="abs center section-title" style="top:80px">GET INSPIRED BY SIMILAR PROJECT</h2>
  <svg class="wave" style="left:410px;top:114px" width="380" height="6"><path d="M0 3 Q4 0 8 3 T16 3 T24 3 T32 3 T40 3 T48 3 T56 3 T64 3 T72 3 T80 3 T88 3 T96 3 T104 3 T112 3 T120 3 T128 3 T136 3 T144 3 T152 3 T160 3 T168 3 T176 3 T184 3 T192 3 T200 3 T208 3 T216 3 T224 3 T232 3 T240 3 T248 3 T256 3 T264 3 T272 3 T280 3 T288 3 T296 3 T304 3 T312 3 T320 3 T328 3 T336 3 T344 3 T352 3 T360 3 T368 3 T376 3" fill="none" stroke="#3e6ad0" stroke-width="1"/></svg>

  <div class="project-card" style="left:181px">
    <svg class="photo" width="256" height="326" role="img" aria-label="Bathroom shower project photo with split overlay"><rect width="256" height="326" fill="#d42424"/><polygon points="0,0 0,326 256,326" fill="#2c4a85"/></svg>
    <h4>PROJECT CORDIAN</h4><div class="project-loc"><svg width="14" height="11"><rect x="0" y="4" width="14" height="7" fill="#6aa3f5"/><circle cx="7" cy="3" r="3" fill="#6aa3f5"/></svg>New year town, Country</div>
  </div>
  <div class="project-card" style="left:472px">
    <svg class="photo" width="256" height="326" role="img" aria-label="Bathroom bathtub project photo with split overlay"><rect width="256" height="326" fill="#d42424"/><polygon points="0,0 0,326 256,326" fill="#2c4a85"/></svg>
    <h4>PROJECT CORDIAN</h4><div class="project-loc"><svg width="14" height="11"><rect x="0" y="4" width="14" height="7" fill="#6aa3f5"/><circle cx="7" cy="3" r="3" fill="#6aa3f5"/></svg>New year town, Country</div>
  </div>
  <div class="project-card" style="left:763px">
    <svg class="photo" width="256" height="326" role="img" aria-label="Bathroom vanity project photo with split overlay"><rect width="256" height="326" fill="#c81a1a"/><polygon points="0,0 0,326 256,326" fill="#243f74"/></svg>
    <h4>PROJECT CORDIAN</h4><div class="project-loc"><svg width="14" height="11"><rect x="0" y="4" width="14" height="7" fill="#6aa3f5"/><circle cx="7" cy="3" r="3" fill="#6aa3f5"/></svg>New year town, Country</div>
  </div>
  <div class="load-more">Load More<br><svg width="10" height="12" fill="none" stroke="#d41c1c" stroke-width="1.5"><path d="M1 1l4 4 4-4M1 6l4 4 4-4"/></svg></div>
</section>

<section class="faq">
  <svg class="bg" width="1200" height="592"><rect width="1200" height="592" fill="#cf1919"/><polygon points="0,0 40,0 1200,592 0,592" fill="#223b66"/></svg>
  <h2 class="faq-title">FREQUENTLY ASKED QUESTION</h2>
  <div class="faq-rule"></div>
  <div class="faq-item" style="top:171px"><div class="faq-q">I care deeply for nature.<svg width="10" height="6" fill="none" stroke="#333" stroke-width="1.6"><path d="M1 1l4 4 4-4"/></svg></div></div>
  <div class="faq-item" style="top:256px"><div class="faq-q">I don't want this thing smelling like fish?<svg width="10" height="6" fill="none" stroke="#333" stroke-width="1.6"><path d="M1 1l4 4 4-4"/></svg></div></div>
  <div class="faq-item open" style="top:343px"><div class="faq-q">I don't want this thing smelling like fish?<svg width="10" height="6" fill="none" stroke="#333" stroke-width="1.6"><path d="M1 1l4 4 4-4"/></svg></div>
    <div class="faq-a">Lorem ipsum dolor sit amet, consectetur adipiscing elit, sed do eiusmod tempor incididunt ut labore et dolore magna aliqua. Quis ipsum suspendisse ultrices gravida.</div></div>
  <div class="faq-item" style="top:471px"><div class="faq-q">I don't want this thing smelling like fish?<svg width="10" height="6" fill="none" stroke="#333" stroke-width="1.6"><path d="M1 1l4 4 4-4"/></svg></div></div>
</section>

<section class="articles">
  <h2 class="abs center section-title" style="top:80px">HELPFUL ARTICLES</h2>
  <svg class="wave" style="left:474px;top:114px" width="252" height="6"><path d="M0 3 Q4 0 8 3 T16 3 T24 3 T32 3 T40 3 T48 3 T56 3 T64 3 T72 3 T80 3 T88 3 T96 3 T104 3 T112 3 T120 3 T128 3 T136 3 T144 3 T152 3 T160 3 T168 3 T176 3 T184 3 T192 3 T200 3 T208 3 T216 3 T224 3 T232 3 T240 3 T248 3" fill="none" stroke="#3e6ad0" stroke-width="1"/></svg>

  <article class="article-card" style="left:164px">
    <div class="article-media" role="img" aria-label="Bright bathroom with freestanding tub and wooden shelf" style="background:linear-gradient(90deg,#ece9e5,#d8cfc4 70%,#8a6a4e)"></div>
    <h5>LOREM IPSUM DOLOR SIT AMERVIDA.</h5>
    <div class="article-meta"><svg width="11" height="11" fill="none" stroke="#3e8bf0" stroke-width="1.3"><rect x=".6" y="2" width="8" height="8.4"/><path d="M4 7l6-6"/></svg>Marlow Denning</div>
    <p>Lorem ipsum dolor sit amet, consectetur adipiscing elit, sed ncididunt ut lt magna aliqua.</p>
    <div class="article-link">Load More »</div>
  </article>
  <article class="article-card" style="left:468px">
    <div class="article-media" role="img" aria-label="Marble bathroom vanity with double sinks" style="background:linear-gradient(180deg,#cfcac4,#8d8377 55%,#cfc9c1)"></div>
    <h5>LOREM IPSUM DOLOR SIT AMERVIDA.</h5>
    <div class="article-meta"><svg width="11" height="11" fill="none" stroke="#3e8bf0" stroke-width="1.3"><rect x=".6" y="2" width="8" height="8.4"/><path d="M4 7l6-6"/></svg>Marlow Denning</div>
    <p>Lorem ipsum dolor sit amet, consectetur adipiscing elit, sed ncididunt ut lt magna aliqua.</p>
    <div class="article-link">Load More »</div>
  </article>
  <article class="article-card" style="left:772px">
    <div class="article-media" role="img" aria-label="White bathroom with tub, plant and wooden stool" style="background:linear-gradient(90deg,#e9ebe8,#7d9a6a 45%,#c9a87f 65%,#e3e3e1)"></div>
    <h5>LOREM IPSUM DOLOR SIT AMERVIDA.</h5>
    <div class="article-meta"><svg width="11" height="11" fill="none" stroke="#3e8bf0" stroke-width="1.3"><rect x=".6" y="2" width="8" height="8.4"/><path d="M4 7l6-6"/></svg>Marlow Denning</div>
    <p>Lorem ipsum dolor sit amet, consectetur adipiscing elit, sed ncididunt ut lt magna aliqua.</p>
    <div class="article-link">Load More »</div>
  </article>
</section>

<footer class="footer">
  <svg class="bg" width="1200" height="366"><rect width="1200" height="366" fill="#b91313"/><polygon points="0,20 1010,366 0,366" fill="#1e3a6a"/></svg>
  <div class="footer-brand"><span class="brand-dot"></span>HEARTHLINE</div>
  <p class="footer-about">Lorem ipsum dolor sit amet, consectetur adipiscing elit, sed do eiusmod tempor incididunt ut labore et dolore magna aliqua.<br><br>Quis ipsum suspendisse ultrices gravida. Risus commodo viverra maecenas accumsan.</p>

  <div class="footer-head" style="left:452px">JOIN OUR COMMUNITY</div>
  <div class="field" style="top:126px">Your Name</div>
  <div class="field" style="top:177px">Your Email</div>
  <div class="btn-submit">Submit</div>

  <div class="footer-head" style="left:716px">SERVICES</div>
  <ul class="footer-list" style="left:716px">
    <li>Basement Finishing</li><li>Bathroom Remodeling</li><li>Handyman</li><li>Kitchen Remodeling</li><li>Window Replacement</li><li>Whole Home Remodeling</li>
  </ul>

  <div class="footer-head" style="left:908px">SERVICE AREAS</div>
  <ul class="footer-list" style="left:908px">
    <li>Brookfall, OR</li><li>Larkmoor, OR</li><li>Fenwick Hollow, OR</li><li>Ashgrove, OR</li><li>Tallowby, OR</li><li>Quenridge, OR</li><li>West Fenwick Hollow, OR</li>
  </ul>

  <div class="copyright">COPYRIGHT ©HEARTHLINE | PRIVACY POLICY | TERMS &amp; CONDITIONS | CONTACT | SITEMAP |</div>
</footer>

</body>
</html>
```